Social Media Graphics - ALL TEXT RK

We are looking for a series of social media graphics for Instagram (standard size 1:1 (1080x1080px) that are ALL TEXT. We want the following quotes below on each graphic; one quote per graphic. AND, In very small letters at the bottom of each graphic, add @RKMarlowLive

The look and feel of these graphics should be complimentary to the color palette attached below; but keep them simple. But the design is up to you; at the end of this document, I provided various samples of all text graphics that I like as examples.

Target Market(s)

women looking to lose weight

Industry/Entity Type

health and wellness

Colors
E54698
E96AAD
F1A4CE
F9D9EA
FCEFF6

Requirements
Must have
• the quotes in the document
Should not have
• no stock photography

```html
<!DOCTYPE html>
<html lang="en">
<head>
<meta charset="utf-8">
<title>RK Social Quote Series</title>
<link href="https://fonts.googleapis.com/css2?family=Comic+Neue:ital,wght@0,700;1,400&display=swap" rel="stylesheet">
<style>
  :root {
    --pink-deep: #FF66B2;
    --pink-mid: #F59BCB;
    --pink-soft: #FBC4E0;
    --pink-light: #FDD5EA;
    --ink: #111111;
    --paper: #FFFFFF;
    --scale: 1.2270;
  }
  html, body {
    margin: 0;
    padding: 0;
    width: 1200px;
    height: 3158px;
    overflow: hidden;
    background: var(--paper);
  }
  .board {
    position: relative;
    width: 978px;
    height: 2574px;
    transform: scale(var(--scale));
    transform-origin: 0 0;
  }
  .tile {
    position: absolute;
    width: 481px;
    height: 480px;
    background: radial-gradient(circle at 50% 50%, var(--pink-light) 0%, var(--pink-soft) 30%, var(--pink-mid) 62%, var(--pink-deep) 100%);
  }
  .col-left { left: 5px; }
  .col-right { left: 494px; }
  .row-1 { top: 18px; }
  .row-2 { top: 533px; }
  .row-3 { top: 1048px; }
  .row-4 { top: 1563px; }
  .row-5 { top: 2078px; }
  .quote-block {
    position: absolute;
    color: var(--ink);
    font-family: "Comic Neue", "Comic Sans MS", cursive;
  }
  .quote {
    margin: 0;
    font-weight: 700;
    font-size: 30px;
    line-height: 33.5px;
    letter-spacing: 0.6px;
    text-transform: uppercase;
  }
  .handle {
    margin: 10px 0 0;
    font-style: italic;
    font-weight: 400;
    font-size: 15px;
    letter-spacing: 0.3px;
    text-transform: uppercase;
    text-align: right;
  }
</style>
</head>
<body>
<main class="board">
  <section class="tile col-left row-1">
    <div class="quote-block" style="left:83px;top:132px;width:340px">
      <p class="quote">Wake up tomorrow with a flatter belly- yes, this overnight remedy works like magic!</p>
      <p class="handle" style="margin-right:22px">@RKMarlowLive</p>
    </div>
  </section>
  <section class="tile col-right row-1">
    <div class="quote-block" style="left:79px;top:124px;width:340px">
      <p class="quote">Struggling with bloating and belly fat? Try this natural solution tonight, and wake up feeling lighter!</p>
      <p class="handle" style="margin-right:12px">@RKMarlowLive</p>
    </div>
  </section>
  <section class="tile col-left row-2">
    <div class="quote-block" style="left:116px;top:114px;width:325px">
      <p class="quote">One supplement, one night; your belly bloat could be gone by morning. Here’s how it works!</p>
      <p class="handle" style="margin-right:22px">@RKMarlowLive</p>
    </div>
  </section>
  <section class="tile col-right row-2">
    <div class="quote-block" style="left:112px;top:156px;width:325px">
      <p class="quote">Finally-a natural solution that flattens your belly and eases stomach bloat</p>
      <p class="handle" style="margin-right:112px">@RKMarlowLive</p>
    </div>
  </section>
  <section class="tile col-left row-3">
    <div class="quote-block" style="left:78px;top:161px;width:340px">
      <p class="quote">Sis, your hormones are out of whack - that’s why the weight won’t budge!</p>
      <p class="handle" style="margin-right:68px">@RKMarlowLive</p>
    </div>
  </section>
  <section class="tile col-right row-3">
    <div class="quote-block" style="left:67px;top:89px;width:362px">
      <p class="quote">Frustrated with belly fat that won’t budge? I’ve got the solution that finally worked for me-no crazy diets required.</p>
      <p class="handle" style="margin-right:48px">@RKMarlowLive</p>
    </div>
  </section>
  <section class="tile col-left row-4">
    <div class="quote-block" style="left:95px;top:155px;width:342px">
      <p class="quote">That stubborn belly fat isn’t your fault - here’s what no one tells you.</p>
      <p class="handle" style="margin-right:52px">@RKMarlowLive</p>
    </div>
  </section>
  <section class="tile col-right row-4">
    <div class="quote-block" style="left:93px;top:156px;width:335px">
      <p class="quote">You’ve been lied to - ‘just eat less and exercise more’ doesn’t work in menopause</p>
      <p class="handle" style="margin-right:6px">@RKMarlowLive</p>
    </div>
  </section>
  <section class="tile col-left row-5">
    <div class="quote-block" style="left:99px;top:113px;width:325px">
      <p class="quote">A natural way to boost GLP-1 - no injections, no side effects, just real results. Here’s how it works</p>
      <p class="handle" style="margin-right:10px">@RKMarlowLive</p>
    </div>
  </section>
  <section class="tile col-right row-5">
    <div class="quote-block" style="left:100px;top:101px;width:335px">
      <p class="quote">GLP-1: the magic behind the weight loss drugs. But here’s the secret - you can boost it naturally without a prescription!</p>
      <p class="handle" style="margin-right:118px">@RKMarlowLive</p>
    </div>
  </section>
</main>
</body>
</html>
```